Business Card for new Architectural Firm

I intend to practice in a rural mountain community in upstate NY, focusing on residential and light commercial projects, including second home / vacation properties. I wish to convey a feeling of rural outdoorsy modernity.

Color is important - bold and urbane. Secondary or tertiary colors preferred.

Font is important, idiosyncratic is ok

Optionally, I may choose to use the name Brackenfold Studio. If used as part of your design, all of the Must Haves are still required.

Images uploaded are logos I like

Industry/Entity Type

Residential

Contact Information for Business Card

Lionel Harwicke
Architect (This word should stand alone or be associated with my name - not license number)
NY License No. 052816
lionel@designlhq.com
607 382 9154

Font styles to use
Sans Serif
Decorative

Requirements
Must have
• Whatever files I need to best utilize your design
• PDF
• JPG
• EPS
• Vectorwhatsit
Nice to have
• Logo or element that can be incorporated into other print material.
• Could be a font based card
Should not have
• no clip art
• No templates
• no floor plans
• no building photographs

```html
<!DOCTYPE html>
<html lang="en">
<head>
<meta charset="utf-8">
<title>Brackenfold Studio — Business Card</title>
<link rel="stylesheet" href="https://fonts.googleapis.com/css2?family=Open+Sans:wght@400;700&family=Rye&family=Special+Elite&display=swap">
<style>
  :root {
    --backdrop: #e9e6e1;
    --card-white: #ffffff;
    --card-white-shade: #eeeeee;
    --forest: #1f8a45;
    --forest-light: #2aa257;
    --forest-dark: #17733a;
    --slate: #7f8d93;
    --slate-light: #97a3a8;
    --slate-text: #6c7a80;
    --ink-white: #ffffff;
    --license-text: #e4e9eb;
  }
  * { margin: 0; padding: 0; box-sizing: border-box; }
  html, body {
    width: 1200px;
    height: 900px;
    overflow: hidden;
    background: var(--backdrop);
  }
  .stage {
    position: relative;
    width: 1200px;
    height: 900px;
  }
  .business-card {
    position: absolute;
    left: 180px;
    top: 210px;
    width: 840px;
    height: 480px;
    overflow: hidden;
    box-shadow: 0 10px 30px rgba(0,0,0,0.18);
    background: linear-gradient(160deg, var(--card-white) 40%, var(--card-white-shade));
  }
  .brand-area {
    position: absolute;
    left: 0; top: 0;
    width: 100%;
    height: 250px;
  }
  .brand-lockup {
    position: absolute;
    left: 300px;
    top: 92px;
    display: flex;
    align-items: center;
    gap: 22px;
  }
  .brand-square {
    width: 78px;
    height: 78px;
    background: var(--forest);
    flex: none;
  }
  .brand-name {
    font-family: "Open Sans", sans-serif;
    font-weight: 700;
    font-size: 38px;
    line-height: 1;
    letter-spacing: 0.5px;
    color: var(--slate-text);
    text-transform: uppercase;
  }
  .brand-tagline {
    margin-top: 10px;
    font-family: "Special Elite", monospace;
    font-size: 20px;
    letter-spacing: 1.5px;
    color: var(--slate-text);
  }
  .contact-band {
    position: absolute;
    left: 0; top: 250px;
    width: 100%;
    height: 160px;
    background: linear-gradient(180deg, var(--forest-light) 0%, var(--forest) 55%, var(--forest-dark) 100%);
    color: var(--ink-white);
  }
  .person-name {
    position: absolute;
    left: 56px;
    top: 24px;
    font-family: "Rye", serif;
    font-size: 40px;
    letter-spacing: 14px;
    text-transform: uppercase;
    white-space: nowrap;
  }
  .contact-lines {
    position: absolute;
    left: 360px;
    top: 86px;
    font-family: "Open Sans", sans-serif;
    font-size: 22px;
    line-height: 32px;
  }
  .license-strip {
    position: absolute;
    left: 0; top: 410px;
    width: 100%;
    height: 70px;
    background: linear-gradient(180deg, var(--slate-light), var(--slate));
  }
  .license-number {
    position: absolute;
    left: 500px;
    top: 22px;
    font-family: "Open Sans", sans-serif;
    font-size: 18px;
    letter-spacing: 0.5px;
    color: var(--license-text);
  }
</style>
</head>
<body>
  <main class="stage">
    <section class="business-card">
      <div class="brand-area">
        <div class="brand-lockup">
          <div class="brand-square"></div>
          <div class="brand-text">
            <div class="brand-name">Brackenfold Studio</div>
            <div class="brand-tagline">Lionel Harwicke Architect</div>
          </div>
        </div>
      </div>
      <div class="contact-band">
        <div class="person-name">Lionel Harwicke</div>
        <div class="contact-lines">
          <div class="contact-email">Email: lionel@designlhq.com</div>
          <div class="contact-phone">Phone: 607 382 9154</div>
        </div>
      </div>
      <div class="license-strip">
        <div class="license-number">NY License No. 052816</div>
      </div>
    </section>
  </main>
</body>
</html>
```